Town of Pellbrook Commercial Development

Create introduction point with 3 subheading categories. The bullets under the 3 categories should be where to use the infographics. Keep the Town of Pellbrook logo in the piece. The layout can be vertical or horizontal. Would like to stay on one page.

Target Market(s)

Commercial real estate developers and corporations

Industry/Entity Type

Real estate

Font styles to use
Serif

Requirements
Must have
• Business to business looking
Should not have
• Not comical

```html
<!DOCTYPE html>
<html lang="en">
<head>
<meta charset="utf-8">
<title>Town of Pellbrook – Commercial Development</title>
<link rel="stylesheet" href="https://fonts.googleapis.com/css2?family=Tinos:ital,wght@0,400;0,700;1,400&family=Arimo:wght@400&display=swap">
<style>
  :root {
    --backdrop: #f4f4f4;
    --paper: #ffffff;
    --ink: #1c1c1c;
    --ink-soft: #333333;
    --brand-red: #8c2a1c;
    --bright-red: #c4301e;
    --rule-red: #b0392b;
    --ring-black: #111111;
    --photo-dark: #1f2420;
    --photo-mid: #3a3d36;
    --photo-warm: #4a3a33;
  }
  * { box-sizing: border-box; margin: 0; padding: 0; }
  html, body { width: 1000px; height: 1200px; overflow: hidden; }
  body { background: var(--backdrop); position: relative; font-family: "Tinos", "Times New Roman", serif; color: var(--ink); }

  .flyer { position: absolute; left: 205px; top: 180px; width: 596px; height: 842px; background: var(--paper); }

  .hero-photo {
    position: absolute; left: 0; top: 0; width: 188px; height: 842px;
    background: linear-gradient(180deg, var(--photo-dark) 0%, var(--photo-mid) 35%, var(--photo-warm) 70%, #2a2420 100%);
  }

  .brand-plate {
    position: absolute; left: 52px; top: 33px; width: 150px; height: 169px;
    background: var(--paper); border-radius: 30px 0 0 30px;
    display: flex; flex-direction: column; align-items: center; justify-content: center; gap: 10px;
  }
  .brand-mark { width: 46px; height: 46px; border-radius: 50%; background: var(--brand-red); }
  .brand-name { font-family: "Tinos", serif; font-weight: 700; font-size: 19px; line-height: 1.1; color: var(--brand-red); text-align: center; }

  .intro {
    position: absolute; left: 283px; top: 57px; width: 290px;
    font-style: italic; font-size: 14.6px; line-height: 22px; color: var(--ink);
  }

  .pillar-letter {
    position: absolute; left: 78px; width: 30px; text-align: center;
    font-size: 38px; color: #ffffff; line-height: 1;
  }

  .pillar-icon {
    position: absolute; left: 135px; width: 104px; height: 104px; border-radius: 50%;
    background: var(--paper); border: 5px solid var(--brand-red);
    display: flex; align-items: center; justify-content: center;
  }
  .pillar-icon.is-community { border-color: var(--bright-red); }
  .pillar-icon.is-business { border-color: var(--ring-black); }

  .pillar { position: absolute; left: 268px; width: 300px; }
  .pillar-title {
    display: flex; align-items: center; gap: 8px;
    font-weight: 700; font-size: 13px; letter-spacing: 0.2px; margin-bottom: 10px;
  }
  .pillar-title::after { content: ""; width: 90px; height: 1px; background: var(--rule-red); }
  .pillar.is-business .pillar-title::after { background: var(--ink); }

  .pillar-list { list-style: none; font-family: "Arimo", Arial, sans-serif; font-size: 8.6px; line-height: 10px; color: var(--ink-soft); }
  .pillar-list li { position: relative; padding-left: 14px; margin-bottom: 6px; width: 285px; }
  .pillar-list li::before {
    content: ""; position: absolute; left: 0; top: 1px; width: 7px; height: 7px; border-radius: 50%;
    border: 1.3px solid var(--bright-red);
    background: radial-gradient(circle, var(--bright-red) 0 1.6px, transparent 1.8px);
  }
  .pillar.is-business .pillar-list li::before {
    border-color: var(--ink);
    background: radial-gradient(circle, var(--ink) 0 1.6px, transparent 1.8px);
  }
</style>
</head>
<body>
  <main class="flyer">
    <div class="hero-photo" role="img" aria-label="Aerial photograph of a white church steeple and brick bell tower rising above a dense green tree canopy, darkened"></div>

    <div class="brand-plate">
      <span class="brand-mark" aria-hidden="true"></span>
      <span class="brand-name">Town of Pellbrook</span>
    </div>

    <p class="intro">Locating your business to Pellbrook could be the smartest move your company ever makes. Our location, employment base, smart growth and college town charm make it a stand-out from other communities.</p>

    <!-- Location -->
    <span class="pillar-letter" style="top:270px">L</span>
    <div class="pillar-icon" style="top:238px">
      <svg width="44" height="52" viewBox="0 0 44 52" fill="none" stroke="#8c2a1c" stroke-width="2">
        <path d="M22 50 C10 34 4 26 4 18 A18 18 0 0 1 40 18 C40 26 34 34 22 50 Z"/>
        <circle cx="22" cy="18" r="7"/>
      </svg>
    </div>
    <section class="pillar" style="top:246px">
      <h2 class="pillar-title">LOCATION</h2>
      <ul class="pillar-list">
        <li>Pellbrook is just 20 miles north of Carverton, NC in Ashby County</li>
        <li>Conveniently located off I-77 and 73</li>
        <li>Within a day’s drive of 40% of the U.S. population, making business close to suppliers and customers alike</li>
        <li>30 minutes from Carverton-Hale International Airport</li>
        <li>Located in the Carverton MSA</li>
        <li>Home of Pellbrook College</li>
        <li>Three hours to beautiful beaches, two hours to scenic mountains</li>
      </ul>
    </section>

    <!-- Community -->
    <span class="pillar-letter" style="top:472px">C</span>
    <div class="pillar-icon is-community" style="top:440px">
      <svg width="58" height="58" viewBox="0 0 58 58" fill="none" stroke="#c4301e" stroke-width="1.8">
        <g>
          <line x1="29" y1="29" x2="9" y2="9"/><line x1="29" y1="29" x2="49" y2="9"/>
          <line x1="29" y1="29" x2="9" y2="49"/><line x1="29" y1="29" x2="49" y2="49"/>
          <line x1="29" y1="29" x2="29" y2="6"/><line x1="29" y1="29" x2="29" y2="52"/>
        </g>
        <g fill="#ffffff">
          <circle cx="29" cy="29" r="9"/>
          <circle cx="9" cy="9" r="6"/><circle cx="49" cy="9" r="6"/>
          <circle cx="9" cy="49" r="6"/><circle cx="49" cy="49" r="6"/>
          <circle cx="29" cy="6" r="5"/><circle cx="29" cy="52" r="5"/>
        </g>
        <circle cx="29" cy="26" r="3"/><path d="M23 35 a6 5 0 0 1 12 0"/>
        <circle cx="9" cy="7.5" r="1.8"/><path d="M5.5 12.5 a3.5 3 0 0 1 7 0"/>
        <circle cx="49" cy="7.5" r="1.8"/><path d="M45.5 12.5 a3.5 3 0 0 1 7 0"/>
        <circle cx="9" cy="47.5" r="1.8"/><path d="M5.5 52.5 a3.5 3 0 0 1 7 0"/>
        <circle cx="49" cy="47.5" r="1.8"/><path d="M45.5 52.5 a3.5 3 0 0 1 7 0"/>
      </svg>
    </div>
    <section class="pillar" style="top:445px">
      <h2 class="pillar-title">COMMUNITY</h2>
      <ul class="pillar-list">
        <li>Pellbrook is one of the fastest growing affluent populations in North Carolina with a median income of $131,144 and population of 15,132</li>
        <li>More than 74% of Pellbrook’s residents over the age of 25 hold a bachelor’s degree or higher</li>
        <li>In national citizen surveys, Pellbrook ranks #1 in “sense of community”</li>
        <li>Pellbrook’s lake amenities, parks, greenways, first-rate schools, low crime rate and proximity to Pellbrook College make it a great place to live and work.</li>
      </ul>
    </section>

    <!-- Business -->
    <span class="pillar-letter" style="top:662px">B</span>
    <div class="pillar-icon is-business" style="top:630px">
      <svg width="60" height="36" viewBox="0 0 60 36" fill="none" stroke="#111111" stroke-width="1.8" stroke-linejoin="round" stroke-linecap="round">
        <path d="M2 8 L10 4 L18 18 L10 22 Z"/>
        <path d="M58 8 L50 4 L42 18 L50 22 Z"/>
        <path d="M13 8 C19 6 23 5 28 7 L36 10"/>
        <path d="M47 8 C42 6 37 6 33 8 L26 13 C24 15 26 18 29 16 L34 13"/>
        <path d="M44 19 L34 13"/>
        <path d="M17 19 L22 24 M21 16 L27 22 M25 14 L31 20 M42 20 C40 24 37 27 33 28 L26 23"/>
        <path d="M17 19 C18 22 20 25 22 24 M27 22 C27 25 30 27 33 28"/>
      </svg>
    </div>
    <section class="pillar is-business" style="top:635px">
      <h2 class="pillar-title">BUSINESS</h2>
      <ul class="pillar-list">
        <li>Pellbrook’s major employers include Varden Technologies, Halcrest Industrial Supply, Ashmore Rand, and Pellbrook College.</li>
        <li>Pellbrook has a thriving Farmer’s Market and is home to over 30 restaurants including Golden Ladle Award nominees.</li>
        <li>Pellbrook promotes a culture of supporting local independent businesses through our active business retention program, various funding programs, and small business networking opportunities.</li>
      </ul>
    </section>
  </main>
</body>
</html>
```